Book cover design for a debut author; 'Quiet Ledgers' by Brent Hollis.

My father has written a book and I would love to gift him a bespoke front cover for it for his 60th birthday this year.
The book is a work of fiction and tells the story of two strangers (an Asian Female and a Caucasian Male) who meet on a train. After the train crashes and bursts into flames, they take the luggage of different passengers and decide to make a new life together, culminating in a murder which they believe they can get away with forever. The book is a thriller and engages the reader in suspense, excitement, anticipation and anxiety.

Target Market(s)

Thriller Fiction Readers

Font styles to use
Serif

Colors

Designer to choose colors to be used in the design.

Requirements
Must have
• A vibrant front cover with consideration over the font of both the title and author.
• I would like the train where they meet to be the main focus for the front cover. The strangers meet on a train and I’d like the cover to reflect this.
• Design must include front cover, spine and back cover with a space for blurb (to follow).
Nice to have
• A photograph based cover would I think suit the book better than an illustration.

```html
<!DOCTYPE html>
<html lang="en">
<head>
<meta charset="utf-8">
<title>Quiet Ledgers — Brent Hollis — Full Cover</title>
<link href="https://fonts.googleapis.com/css2?family=Cinzel:wght@400;500&family=Josefin+Sans:wght@400;600;700&display=swap" rel="stylesheet">
<style>
  :root {
    --page-bg: #ffffff;
    --night-deep: #0d0f14;
    --night-mid: #1d2129;
    --night-haze: #3a3f48;
    --smoke-pale: #9aa3b6;
    --smoke-grey: #7c869c;
    --smoke-blue: #5468a8;
    --forest-dark: #16181c;
    --ground: #2a2724;
    --gold: #f2b620;
    --gold-light: #ffd95a;
    --gold-deep: #c98a0c;
    --text-light: #f2f2f2;
    --frame-white: #ffffff;
  }
  * { margin: 0; padding: 0; box-sizing: border-box; }
  html, body { width: 1200px; height: 1200px; overflow: hidden; background: var(--page-bg); }
  .canvas { position: relative; width: 1200px; height: 1200px; background: var(--page-bg); }
  .cover-wrap { position: absolute; left: 0; top: 136px; width: 1200px; height: 870px; overflow: hidden; }

  /* Back cover */
  .back-cover { position: absolute; left: 0; top: 0; width: 580px; height: 870px; }
  .back-photo {
    position: absolute; inset: 0;
    background:
      radial-gradient(ellipse at 50% 15%, var(--night-haze) 0%, transparent 55%),
      radial-gradient(ellipse at 45% 95%, #3b3225 0%, transparent 40%),
      linear-gradient(180deg, var(--night-mid) 0%, var(--night-deep) 55%, #16140f 100%);
  }
  .section-heading {
    position: absolute; left: 70px; width: 442px; text-align: center;
    font-family: 'Josefin Sans', sans-serif; font-weight: 700; font-size: 15.5px; color: var(--gold);
  }
  .blurb {
    position: absolute; left: 70px; width: 442px;
    font-family: 'Josefin Sans', sans-serif; font-size: 13.8px; line-height: 21px;
    color: var(--text-light); text-align: justify;
  }
  .author-photo-frame {
    float: left; width: 94px; height: 122px; margin: 2px 10px 6px 0;
    border: 3px solid var(--frame-white);
  }

  /* Spine */
  .spine {
    position: absolute; left: 580px; top: 0; width: 40px; height: 870px;
    background: linear-gradient(180deg, #2a2d33 0%, #121418 60%, #2b2519 100%);
    display: flex; justify-content: center; padding-top: 214px;
  }
  .spine-text {
    writing-mode: vertical-rl; white-space: nowrap;
    font-family: 'Cinzel', serif; font-size: 29px; color: var(--gold); letter-spacing: 1px;
  }
  .spine-author { font-family: 'Josefin Sans', sans-serif; font-size: 29px; font-weight: 600; color: var(--text-light); letter-spacing: 0; }

  /* Front cover */
  .front-cover { position: absolute; left: 620px; top: 0; width: 580px; height: 870px; }
  .front-photo {
    position: absolute; inset: 0;
    background:
      radial-gradient(ellipse 46% 34% at 58% 44%, var(--smoke-blue) 0%, transparent 100%),
      radial-gradient(ellipse 70% 45% at 55% 22%, var(--smoke-pale) 0%, transparent 100%),
      linear-gradient(90deg, var(--forest-dark) 0%, transparent 22%, transparent 78%, var(--forest-dark) 100%),
      linear-gradient(180deg, var(--smoke-grey) 0%, #5c6782 42%, #262a33 72%, var(--forest-dark) 88%, var(--ground) 100%);
  }
  .title-art { position: absolute; left: 0; top: 0; width: 580px; height: 870px; }
  .front-author {
    position: absolute; left: 0; width: 580px; top: 752px; text-align: center;
    font-family: 'Josefin Sans', sans-serif; font-weight: 600; font-size: 46px; color: var(--text-light);
    padding-left: 20px;
  }
</style>
</head>
<body>
<div class="canvas">
  <div class="cover-wrap">
    <section class="back-cover">
      <div class="back-photo" role="img" aria-label="Photograph of a starry night sky with smoke haze over railway tracks"></div>
      <h2 class="section-heading" style="top: 83px;">About the author</h2>
      <div class="blurb" style="top: 116px;">
        <div class="author-photo-frame"></div>
        “At vero eos et accusamus et iusto odio dignissimos ducimus qui blanditiis praesentium voluptatum deleniti atque corrupti quos dolores et quas molestias excepturi sint occaecati cupiditate non provident, similique sunt in culpa qui officia deserunt mollitia animi, id est laborum et dolorum fuga. Et harum quidem rerum facilis est et expedita distinctio. Nam libero tempore, cum soluta nobis est eligendi optio cumque nihil impedit quo minus id quod maxime placeat facere possimus, omnis voluptas assumenda est, omnis dolor repellendus. Temporibus autem quibusdam et aut officiis debitis aut rerum necessitatibus saepe eveniet ut et voluptates repudiandae sint et molestiae non recusandae. Itaque earum rerum hic tenetur a sapiente delectus, ut aut reiciendis voluptatibus maiores alias consequatur aut perferendis doloribus asperiores repellat."
      </div>
      <h2 class="section-heading" style="top: 454px;">About the book</h2>
      <p class="blurb" style="top: 486px;">
        “At vero eos et accusamus et iusto odio dignissimos ducimus qui blanditiis praesentium voluptatum deleniti atque corrupti quos dolores et quas molestias excepturi sint occaecati cupiditate non provident, similique sunt in culpa qui officia deserunt mollitia animi, id est laborum et dolorum fuga. Et harum quidem rerum facilis est et expedita distinctio. Nam libero tempore, cum soluta nobis est eligendi optio cumque nihil impedit quo minus id quod maxime placeat facere possimus, omnis voluptas assumenda est, omnis dolor repellendus. Temporibus autem quibusdam et aut officiis debitis aut rerum necessitatibus saepe eveniet ut et voluptates repudiandae sint et molestiae non recusandae. Itaque earum rerum hic tenetur a sapiente delectus, ut aut reiciendis voluptatibus maiores alias consequatur aut perferendis doloribus asperiores repellat."
      </p>
    </section>

    <aside class="spine">
      <span class="spine-text">QUIET LEDGERS - <span class="spine-author">Brent Hollis</span></span>
    </aside>

    <section class="front-cover">
      <div class="front-photo" role="img" aria-label="Photograph of a steam locomotive with glowing headlamp under a towering cloud of blue-grey smoke, on tracks through a dark winter forest"></div>
      <svg class="title-art" viewBox="0 0 580 870" role="img" aria-label="Quiet Ledgers">
        <defs>
          <linearGradient id="gold-fill" x1="0" y1="0" x2="1" y2="1">
            <stop offset="0" stop-color="#c98a0c"/>
            <stop offset="0.35" stop-color="#ffd95a"/>
            <stop offset="0.6" stop-color="#f2b620"/>
            <stop offset="1" stop-color="#c98a0c"/>
          </linearGradient>
        </defs>
        <text x="34" y="166" textLength="426" lengthAdjust="spacingAndGlyphs" font-family="Cinzel, serif" font-size="128" fill="url(#gold-fill)">QUIET</text>
        <text x="20" y="280" textLength="516" lengthAdjust="spacingAndGlyphs" font-family="Cinzel, serif" font-size="118" fill="url(#gold-fill)">LEDGERS</text>
      </svg>
      <div class="front-author">Brent Hollis</div>
    </section>
  </div>
</div>
</body>
</html>
```